Website front page and logo re-designed (using logo provided)

We are looking for the home page of our new website. It is a website offering a space for clients to ask professionals questions. The website should be similar in design to www.brimtolo.com however it is clear it should be a different look. It should be modern, simple to use, a clear navigation bar at the top and bottom.

Logo should be similar to the one attached, but more professional and modern. Logo should be clearly incorporated into website. Design should focus on our website colours as in the logo.

Logo Text

Kelvora - Clarity at every turn!

Number of Pages Required

1 page

Font styles to use
Sans Serif

```html
<!DOCTYPE html>
<html lang="en">
<head>
<meta charset="utf-8">
<title>Kelvora – Clarity at every turn!</title>
<link rel="stylesheet" href="https://fonts.googleapis.com/css2?family=Jost:wght@400;500;600&family=Open+Sans:wght@400;600&display=swap">
<style>
:root{
  --brand:#d4561f;
  --brand-dark:#b9471a;
  --ink:#161616;
  --text:#555;
  --muted:#8a8a8a;
  --light:#f0f0f0;
  --dark:#2b2b2b;
  --black:#050505;
  --white:#fff;
}
*{box-sizing:border-box;margin:0;padding:0}
html,body{width:1200px;height:2161px;overflow:hidden}
body{position:relative;background:var(--white);font-family:"Open Sans",Arial,sans-serif;color:var(--text)}
.abs{position:absolute}
a{color:inherit;text-decoration:none}

/* header */
.site-header{position:absolute;left:0;top:0;width:1200px;height:118px;background:var(--white)}
.brand{position:absolute;left:48px;top:18px;display:flex;align-items:center;gap:14px}
.brand-dot{width:80px;height:80px;border-radius:50%;background:var(--brand)}
.brand-name{font-family:"Jost",sans-serif;font-weight:600;font-size:40px;color:var(--brand);letter-spacing:.5px}
.main-nav a{position:absolute;top:0;height:118px;line-height:106px;font-size:14px;color:#666}
.main-nav .active{left:634px;width:79px;background:var(--brand);color:var(--white);text-align:center;font-weight:600}

/* hero */
.hero{position:absolute;left:0;top:118px;width:1200px;height:489px;background:linear-gradient(90deg,#ebe8ec 0%,#f1eff2 45%,#e4e1e4 100%)}
.hero-photo{position:absolute;right:0;top:0;width:460px;height:489px;background:radial-gradient(ellipse at 55% 35%,#e3c6b3 0%,#cdb0a0 30%,#9aa4bb 62%,#6f7d9c 100%)}
.hero-title{position:absolute;left:98px;top:122px;font-family:"Jost",sans-serif;font-weight:500;font-size:56px;line-height:68px;color:var(--ink)}
.hero-title em{font-style:normal;color:var(--brand)}
.hero-copy{position:absolute;left:98px;top:270px;width:580px;font-size:12px;line-height:21px;color:#333}
.btn{position:absolute;background:var(--brand);color:var(--white);font-size:12px;text-align:center;font-family:"Open Sans",sans-serif}
.hero .btn{left:98px;top:336px;width:118px;height:46px;line-height:46px}
.slider-dots{position:absolute;left:468px;top:413px;display:flex;gap:8px}
.slider-dots span{width:13px;height:13px;border:1.5px solid var(--brand);border-radius:50%}
.slider-dots .on{background:var(--brand)}
.arrow{position:absolute;top:231px;width:36px;height:36px;border-radius:50%;background:var(--white);box-shadow:0 1px 3px rgba(0,0,0,.2)}
.arrow svg{position:absolute;left:12px;top:11px}

/* ask bar */
.ask-bar{position:absolute;left:0;top:607px;width:1200px;height:151px;background:var(--dark)}
.topics{position:absolute;left:48px;top:24px;font-size:14px;color:#e6e6e6;word-spacing:2px}
.topics span{margin:0 12px;color:#bbb}
.ask-field{position:absolute;left:48px;top:50px;width:798px;height:81px;border:1px solid #777;padding:14px 10px;font-size:13px;color:#999}
.online{position:absolute;left:897px;top:30px;width:266px;text-align:center;font-size:12px;color:#eee}
.ask-btn{position:absolute;left:897px;top:54px;width:266px;height:75px;background:var(--brand);border:1px solid #e88a5c;color:var(--white);font-family:"Jost",sans-serif;font-weight:500;font-size:21px;text-align:center;padding-top:40px;letter-spacing:.5px}
.ask-btn svg{position:absolute;left:120px;top:12px}

/* welcome */
.welcome h1{position:absolute;left:0;top:814px;width:1200px;text-align:center;font-family:"Jost",sans-serif;font-weight:500;font-size:29px;color:var(--ink)}
.welcome h1 em{font-style:normal;color:var(--brand)}
.welcome p{position:absolute;left:120px;top:868px;width:960px;text-align:center;font-size:12px;line-height:21px;color:#555}
.welcome .btn{left:539px;top:958px;width:125px;height:39px;line-height:39px}

/* experts */
.experts{position:absolute;left:0;top:1043px;width:1200px;height:406px;background:var(--light)}
.expert{position:absolute;width:300px}
.expert h3{font-family:"Jost",sans-serif;font-weight:500;font-size:20px;color:var(--brand);margin-bottom:6px}
.expert p{font-size:11.5px;line-height:20px;color:#777}
.expert .more{display:block;margin-top:4px;font-size:11px;font-weight:600;color:#333}
.expert.left{text-align:right}
.expert .more.hot{color:var(--brand)}
.badge{position:absolute;width:118px;height:118px;border-radius:50%;background:var(--white);border:2px solid var(--brand)}
.badge::after{content:"";position:absolute;left:6px;top:6px;width:102px;height:102px;border-radius:50%;border:1px solid #ddd}
.badge.fill{background:var(--white)}
.badge.fill::after{background:var(--brand);border-color:var(--brand)}
.badge svg{position:absolute;left:34px;top:34px;z-index:1}

/* help */
.help{position:absolute;left:0;top:1449px;width:1200px;height:329px;background:linear-gradient(100deg,#d97a4f 0%,#cf6c41 40%,#c65c30 70%,#b9532a 100%)}
.help h2{position:absolute;left:0;top:48px;width:1200px;text-align:center;font-family:"Jost",sans-serif;font-weight:500;font-size:28px;color:var(--white)}
.help-item{position:absolute;top:122px;width:220px;text-align:center;color:var(--white);font-family:"Jost",sans-serif;font-weight:500;font-size:20px}
.help-item .ring{width:104px;height:104px;margin:0 auto 18px;border:2px solid var(--white);border-radius:50%;position:relative}
.help-item svg{position:absolute;left:32px;top:32px}

/* footer */
.site-footer{position:absolute;left:0;top:1778px;width:1200px;height:288px;background:var(--white)}
.site-footer .brand{left:66px;top:90px}
.site-footer .brand-dot{width:100px;height:100px}
.site-footer .brand-name{font-size:44px}
.f-col{position:absolute;top:34px;height:220px;border-left:1px solid #e2e2e2;padding-left:31px}
.f-col h4{font-family:"Jost",sans-serif;font-weight:500;font-size:17px;color:var(--brand);margin:24px 0 12px}
.f-col li{list-style:none;font-size:11.5px;color:var(--muted);line-height:29px}
.f-col li::before{content:"•";margin-right:8px;color:#aaa}

.bottom-bar{position:absolute;left:0;top:2066px;width:1200px;height:95px;background:var(--black)}
.bottom-bar p{position:absolute;left:0;top:40px;width:1200px;text-align:center;font-size:11.5px;color:var(--white)}
.social{position:absolute;top:35px;width:29px;height:29px;border:1.5px solid var(--brand)}
</style>
</head>
<body>

<header class="site-header">
  <a class="brand" href="#"><span class="brand-dot"></span><span class="brand-name">Kelvora</span></a>
  <nav class="main-nav">
    <a class="active" href="#">Home</a>
    <a style="left:749px" href="#">About Us</a>
    <a style="left:864px" href="#">Services</a>
    <a style="left:969px" href="#">Testimonial</a>
    <a style="left:1095px" href="#">Contact</a>
  </nav>
</header>

<section class="hero">
  <div class="hero-photo" role="img" aria-label="Photo of a smiling professional adviser resting his chin on his hand"></div>
  <h2 class="hero-title">Get an <em>Answer Quick..</em><br>Ask your <em>Question</em></h2>
  <p class="hero-copy">Lorem ipsum dolor sit amet, consectetur adipiscing elit, sed do eiusmod tempor incididunt ut labore et dolore magna aliqua. Ut enim consectetur adipiscing elitad minim veniam labour.</p>
  <a class="btn" href="#">READ MORE</a>
  <div class="slider-dots"><span></span><span></span><span class="on"></span><span></span><span></span></div>
  <span class="arrow" style="left:30px"><svg width="12" height="14" viewBox="0 0 12 14"><path d="M8 1 2 7l6 6" fill="none" stroke="#222" stroke-width="2.2"/></svg></span>
  <span class="arrow" style="left:1134px"><svg width="12" height="14" viewBox="0 0 12 14"><path d="M3 1l6 6-6 6" fill="none" stroke="#222" stroke-width="2.2"/></svg></span>
</section>

<section class="ask-bar">
  <div class="topics">Lawyers<span>|</span>Mechanics<span>|</span>Doctors &amp; Nurses<span>|</span>Vets<span>|</span>Electricians &amp; Plumbers<span>|</span>Computer &amp; Eductation</div>
  <div class="ask-field">Choose an Expert and type your question here...</div>
  <div class="online">52 EXPERTS ARE ONLINE NOW</div>
  <a class="ask-btn" href="#"><svg width="26" height="22" viewBox="0 0 26 22"><path d="M1 10 25 1l-6 20-6-8z" fill="#fff"/><path d="M13 13 25 1" stroke="#d4561f" stroke-width="1.5"/></svg>GET AN ANSWER</a>
</section>

<section class="welcome">
  <h1>WELCOME TO <em>Kelvora</em></h1>
  <p>Lorem ipsum dolor sit amet, consectetur adipiscing elit, sed do eiusmod tempor incididunt ut labore et dolore magna aliqua. Ut enim ad minim veniam, quis nostrud exercitation ullamco laboris nisi ut aliquip ex ea commodo consequat. Duis aute irure dolor in reprehenderit in voluptate velit esse cillum dolore eu fugiat nulla pariatur. Excepteur sint occaecat cupidatat non proident, sunt in culpa qui officia deserunt mollit anim id est laborum.</p>
  <a class="btn" href="#">READ MORE</a>
</section>

<section class="experts">
  <div class="expert left" style="left:131px;top:51px">
    <h3>Arlen Hoke</h3>
    <p>Lorem ipsum dolor sit amet, consectetur adipiscing elit, sed do eiusmod tempor incididunt ut labore et dolore magna aliqua. Ut enim ad minim veniam...</p>
    <a class="more hot" href="#">READ MORE ▸</a>
  </div>
  <div class="badge fill" style="left:444px;top:50px"><svg width="50" height="50" viewBox="0 0 50 50"><circle cx="25" cy="13" r="9" fill="#fff"/><path d="M6 48c0-14 8-20 19-20s19 6 19 20z" fill="#fff"/><path d="M18 30v8a4 4 0 0 0 8 0M32 30v7" stroke="#d4561f" stroke-width="2.5" fill="none"/><circle cx="32" cy="40" r="3" fill="none" stroke="#d4561f" stroke-width="2.5"/></svg></div>

  <div class="badge" style="left:643px;top:50px"><svg width="50" height="50" viewBox="0 0 50 50" fill="#777"><rect x="23.5" y="4" width="3" height="38"/><rect x="14" y="42" width="22" height="4"/><rect x="6" y="9" width="38" height="2.5"/><path d="M9 11 3 26h12zM41 11l-6 15h12z" fill="none" stroke="#777" stroke-width="1.5"/><path d="M2 26a7 5 0 0 0 14 0zM34 26a7 5 0 0 0 14 0z"/></svg></div>
  <div class="expert" style="left:782px;top:51px">
    <h3>Corwin Vale</h3>
    <p>Lorem ipsum dolor sit amet, consectetur adipiscing elit, sed do eiusmod tempor incididunt ut labore et dolore magna aliqua. Ut enim ad minim veniam...</p>
    <a class="more" href="#">READ MORE ▸</a>
  </div>

  <div class="expert left" style="left:131px;top:212px">
    <h3>Tovin Rask</h3>
    <p>Lorem ipsum dolor sit amet, consectetur adipiscing elit, sed do eiusmod tempor incididunt ut labore et dolore magna aliqua. Ut enim ad minim veniam...</p>
    <a class="more" href="#">READ MORE ▸</a>
  </div>
  <div class="badge" style="left:444px;top:212px"><svg width="50" height="50" viewBox="0 0 50 50" fill="#777"><rect x="23.5" y="4" width="3" height="38"/><rect x="14" y="42" width="22" height="4"/><rect x="6" y="9" width="38" height="2.5"/><path d="M9 11 3 26h12zM41 11l-6 15h12z" fill="none" stroke="#777" stroke-width="1.5"/><path d="M2 26a7 5 0 0 0 14 0zM34 26a7 5 0 0 0 14 0z"/></svg></div>

  <div class="badge" style="left:643px;top:212px"><svg width="50" height="50" viewBox="0 0 50 50"><circle cx="25" cy="13" r="9" fill="#777"/><path d="M6 48c0-14 8-20 19-20s19 6 19 20z" fill="#777"/><path d="M18 30v8a4 4 0 0 0 8 0M32 30v7" stroke="#fff" stroke-width="2.5" fill="none"/><circle cx="32" cy="40" r="3" fill="none" stroke="#fff" stroke-width="2.5"/></svg></div>
  <div class="expert" style="left:782px;top:212px">
    <h3>Marek Doyle</h3>
    <p>Lorem ipsum dolor sit amet, consectetur adipiscing elit, sed do eiusmod tempor incididunt ut labore et dolore magna aliqua. Ut enim ad minim veniam...</p>
    <a class="more" href="#">READ MORE ▸</a>
  </div>
</section>

<section class="help" role="img" aria-label="Orange-toned photo of two people shaking hands beside a tablet">
  <h2>Just in Case You Need Any Help</h2>
  <div class="help-item" style="left:63px"><div class="ring"><svg width="40" height="40" viewBox="0 0 40 40"><rect x="3" y="9" width="34" height="23" rx="2" fill="#fff"/><path d="M3 11l17 12 17-12" fill="none" stroke="#cf6c41" stroke-width="2"/></svg></div>EMAIL SUPPORT</div>
  <div class="help-item" style="left:341px"><div class="ring"><svg width="40" height="40" viewBox="0 0 40 40"><rect x="11" y="3" width="18" height="34" rx="3" fill="none" stroke="#fff" stroke-width="2.5"/><rect x="14" y="8" width="12" height="21" fill="#fff"/><circle cx="20" cy="33" r="1.6" fill="#fff"/></svg></div>FREE PHONE</div>
  <div class="help-item" style="left:619px"><div class="ring"><svg width="40" height="40" viewBox="0 0 40 40"><path d="M30 4a9 9 0 0 0-9 11L6 30a3.5 3.5 0 0 0 5 5l15-15a9 9 0 0 0 11-9l-6 4-5-5z" fill="#fff"/></svg></div>24/7 SUPPORT</div>
  <div class="help-item" style="left:900px"><div class="ring"><svg width="40" height="40" viewBox="0 0 40 40"><text x="20" y="32" text-anchor="middle" font-family="Jost,sans-serif" font-weight="600" font-size="34" fill="#fff">?</text></svg></div>FAQ</div>
</section>

<footer class="site-footer">
  <a class="brand" href="#"><span class="brand-dot"></span><span class="brand-name">Kelvora</span></a>
  <div class="f-col" style="left:373px"><h4>Important Links</h4><ul><li>Affiliate Program</li><li>Special Promotions</li><li>Newsletter</li><li>Contact</li></ul></div>
  <div class="f-col" style="left:653px"><h4>Categories</h4><ul><li>Webmail Login</li><li>Account Login</li><li>FAQs</li><li>Server References</li></ul></div>
  <div class="f-col" style="left:934px"><h4>Navigation</h4><ul><li>About Us</li><li>Services</li><li>Careers</li><li>How it work</li><li>Contact Us</li></ul></div>
</footer>

<div class="bottom-bar">
  <p>Copyright 2015 Company Name.&nbsp; All Rights Reserved.</p>
  <span class="social" style="left:1037px"></span>
  <span class="social" style="left:1080px;background:var(--brand)"></span>
  <span class="social" style="left:1124px"></span>
</div>

</body>
</html>
```